Medical Services company. Need a website that blows the competition out of the water

We need a web site designed to draw attention to our many services offered. We are a Medical Services business based out of Pennsylvania. We provide basic first aid staffing for events and businesses such as but not limited to: Fairs, Festivals, Carnivals, Sporting events, Large gatherings where a first aid station is needed, Concerts, Businesses with first aid needs . We provide training and certifications that are tailored to the customers needs. We provide Covid-19 pre screening and temperature monitoring. Our professionals consist of individuals with Basic First Aid, Certified Nursing Assistants, Medical Assistants, Emergency Medical Responders (EMR), Emergency Medical Technicians (EMT), and Nurses. I do not know how many pages I will need since we offer multiple different services. Our main services provided are: First Aid services, Covid-19 pre screen and temperatures, and Training/Certifications. You will have to use stock photos for now until I can get some actual photographs of our team.I have uploaded a copy of my brochure so you can get some information from there as well.

Target Market(s)

-For the first Aid and Covid-19 services: All Businesses, Sporting events, Event organizers
-Training: Everyone.

Coding

Number of Pages Required

Font styles to use
Sans Serif

Requirements
Must have
• My colors are what is in the logos and Gray , need to have a way for customers to request a quote, design that grabs their attention. Should have pictures of medical providers attending to the sick or injured. Both in a office setting and in an emergency out in public. Should have pictures of an ambulance. Should also have pictures of staff taking temperatures and asking pre screening questions.
Nice to have
• I'll get back to you on that one

```html
<!DOCTYPE html>
<html lang="en">
<head>
<meta charset="utf-8">
<title>KMT Medical Services</title>
<link rel="stylesheet" href="https://fonts.googleapis.com/css2?family=Cinzel:wght@600;700&family=Open+Sans:wght@400;600;700&display=swap">
<style>
:root{
  --blue:#2b36b3;
  --blue-dark:#1f2690;
  --purple-a:#6a5ad8;
  --purple-b:#3a3fc0;
  --teal:#1ec6ad;
  --ink:#333844;
  --muted:#6d7280;
  --gray-bg:#e6e6e8;
  --footer:#2b2c30;
  --footer-bottom:#1f2023;
  --white:#ffffff;
}
*{box-sizing:border-box;margin:0;padding:0}
html,body{width:1200px;height:3128px;overflow:hidden}
body{font-family:"Open Sans",Arial,sans-serif;color:var(--ink);background:var(--white);position:relative}
.heading{font-family:"Cinzel",Georgia,serif;font-weight:700;letter-spacing:2px}

/* header */
.site-header{height:112px;display:flex;align-items:center;justify-content:space-between;padding:0 44px;background:var(--white)}
.brand{display:flex;align-items:center;gap:14px}
.brand-dot{width:56px;height:56px;border-radius:50%;background:var(--blue)}
.brand-name{font-family:"Open Sans",sans-serif;font-weight:700;font-size:30px;color:var(--blue);line-height:1}
.main-nav{display:flex;gap:34px;font-size:15px;font-weight:600;color:#4a4f5c;text-transform:uppercase}
.main-nav a{text-decoration:none;color:inherit;padding-bottom:6px}
.main-nav a.active{color:var(--blue);border-bottom:3px solid var(--blue)}

/* hero */
.hero{position:relative;height:608px;text-align:center;color:var(--white)}
.hero-photo{position:absolute;inset:0;background:radial-gradient(ellipse at 65% 55%,#6d6355 0%,#3a3632 35%,#1a1b1f 75%)}
.hero-content{position:relative;padding-top:200px}
.hero-title{font-size:68px;letter-spacing:4px}
.hero-sub{font-size:26px;margin-top:6px}
.btn-teal{display:inline-block;margin-top:30px;background:var(--teal);color:var(--white);font-weight:700;font-size:15px;padding:14px 30px;border-radius:30px;text-transform:uppercase}
.dots{position:absolute;bottom:22px;left:0;right:0;display:flex;justify-content:center;gap:10px}
.dots span{width:10px;height:10px;border-radius:50%;background:rgba(255,255,255,.5)}
.dots span.on{background:var(--white)}

/* welcome */
.welcome{height:520px;background:linear-gradient(135deg,var(--purple-a),var(--purple-b));color:var(--white);position:relative;padding:120px 0 0 80px}
.welcome h2{font-size:46px}
.welcome p{width:540px;font-size:15px;line-height:1.6;margin-top:18px;opacity:.9}
.btn-outline{display:inline-block;border:2px solid var(--white);color:var(--white);border-radius:30px;padding:12px 28px;font-size:14px;font-weight:700;margin-top:30px}
.welcome-art{position:absolute;left:700px;top:60px;width:420px;height:400px;border-radius:50%;background:radial-gradient(circle,#e9eef6 0%,#8aa4c8 55%,rgba(106,90,216,0) 72%)}

/* professionals */
.professionals{height:580px;text-align:center;padding-top:78px;position:relative}
.section-title{font-size:46px;color:var(--blue)}
.pro-row{display:flex;justify-content:center;gap:40px;margin-top:56px}
.pro-card{width:230px}
.icon-ring{width:128px;height:128px;border-radius:50%;background:var(--blue);border:6px solid #d8dbf3;margin:0 auto;display:flex;align-items:center;justify-content:center}
.pro-card h3{font-size:14px;color:var(--blue);font-weight:700;text-transform:uppercase;margin-top:18px}
.pro-card p{font-size:11.5px;line-height:1.55;color:var(--muted);margin-top:10px}
.btn-small{display:inline-block;margin-top:20px;border:2px solid var(--blue);color:var(--blue);font-weight:700;font-size:12px;padding:8px 18px;border-radius:20px}
.arrow{position:absolute;top:340px}
.arrow.left{left:44px}.arrow.right{right:44px}

/* services */
.services{height:464px;position:relative;color:var(--white);text-align:center;padding-top:68px}
.services-photo{position:absolute;inset:0;background:linear-gradient(rgba(34,44,150,.85),rgba(34,44,150,.85)),linear-gradient(90deg,#7b8aa6,#c9d0dc 55%,#5c6b86)}
.services>*:not(.services-photo){position:relative}
.services .section-title{color:var(--white)}
.services-intro{width:840px;margin:12px auto 0;font-size:12.5px;line-height:1.6;opacity:.9}
.service-row{display:flex;justify-content:center;gap:40px;margin-top:36px}
.service-row>div{width:320px}
.service-row .ring{width:150px;height:150px;border-radius:50%;background:var(--white);display:flex;align-items:center;justify-content:center;margin:0 auto}
.service-row h3{font-size:21px;font-weight:400;margin-top:18px}

/* testimonials */
.testimonials{height:456px;background:var(--gray-bg);text-align:center;padding-top:70px;position:relative}
.testimonials .section-title{color:var(--blue)}
.client-photo{width:112px;height:112px;border-radius:50%;margin:26px auto 0;background:linear-gradient(135deg,#d9b58f,#9c7b5e)}
.quote{width:780px;margin:26px auto 0;font-size:13px;font-style:italic;line-height:1.7;color:var(--muted)}
.client-name{margin-top:22px;font-family:"Cinzel",serif;font-weight:600;font-size:15px;color:var(--teal)}
.testimonials .dots span{background:#b9bcc4}
.testimonials .dots span.on{background:var(--blue)}
.qmark{position:absolute;top:228px;font-size:90px;color:#cfd1d7;font-family:Georgia,serif}

/* footer */
.site-footer{height:340px;background:var(--footer);color:#cfd1d6;display:flex;padding:64px 60px 0;gap:0}
.footer-col h4{font-size:15px;color:var(--white);text-transform:uppercase;letter-spacing:1px;margin-bottom:22px}
.quick{width:420px}
.quick ul{list-style:none;display:grid;grid-template-columns:180px 180px;row-gap:12px;font-size:13px}
.contact{width:400px}
.contact-line{display:flex;gap:12px;align-items:flex-start;font-size:13px;margin-bottom:16px;line-height:1.5}
.connect{flex:1;text-align:center}
.social{display:flex;justify-content:center;gap:12px}
.social span{width:34px;height:34px;border-radius:50%;background:#4a4b52}
.footer-badge{width:80px;height:80px;border-radius:50%;background:#3f4048;margin:28px auto 0}
.footer-bottom{height:48px;background:var(--footer-bottom);color:#8d9098;font-size:11px;display:flex;align-items:center;justify-content:space-between;padding:0 60px}
</style>
</head>
<body>

<header class="site-header">
  <div class="brand"><span class="brand-dot"></span><span class="brand-name">KMT Medical Services</span></div>
  <nav class="main-nav">
    <a class="active" href="#">Home</a><a href="#">About Us</a><a href="#">Our Professionals</a><a href="#">KMT Services</a><a href="#">Our Team</a><a href="#">Contact Us</a>
  </nav>
</header>

<section class="hero">
  <div class="hero-photo" role="img" aria-label="Paramedics loading a stretcher into an ambulance at night"></div>
  <div class="hero-content">
    <h1 class="hero-title heading">KMT MEDICAL SERVICES</h1>
    <p class="hero-sub">We are Medical Professionals providing you with professional services</p>
    <span class="btn-teal">Contact Us</span>
  </div>
  <div class="dots"><span></span><span class="on"></span><span></span><span></span></div>
</section>

<section class="welcome">
  <h2 class="heading">WELCOME TO KMT</h2>
  <p>Our team brings trained first aid staff to fairs, festivals, concerts, sporting events and workplaces across the region. We set up fully stocked stations, respond quickly to injuries and illness, and keep organizers informed from the first hour to the last.</p>
  <p>We also offer tailored training and certification courses, plus Covid-19 pre screening and temperature checks, so every guest and employee can take part with confidence and peace of mind.</p>
  <span class="btn-outline">LEARN MORE</span>
  <div class="welcome-art" role="img" aria-label="Collage of medical staff photos arranged in a star shape"></div>
</section>

<section class="professionals">
  <h2 class="section-title heading">OUR PROFESSIONALS</h2>
  <svg class="arrow left" width="20" height="34" viewBox="0 0 20 34"><path d="M17 3 3 17l14 14" fill="none" stroke="#9aa0ad" stroke-width="3"/></svg>
  <svg class="arrow right" width="20" height="34" viewBox="0 0 20 34"><path d="M3 3l14 14L3 31" fill="none" stroke="#9aa0ad" stroke-width="3"/></svg>
  <div class="pro-row">
    <div class="pro-card">
      <div class="icon-ring"><svg width="60" height="44" viewBox="0 0 60 44" fill="none" stroke="#fff" stroke-width="3"><rect x="2" y="6" width="36" height="26" rx="2"/><path d="M38 14h10l9 10v8H38"/><circle cx="14" cy="36" r="5"/><circle cx="46" cy="36" r="5"/><path d="M20 12v14M13 19h14"/></svg></div>
      <h3>Emergency Medical Technicians (EMT)</h3>
      <p>Our technicians respond fast on site, assess patients, stabilize injuries and coordinate transport with local hospitals whenever further care is needed.</p>
      <span class="btn-small">LEARN MORE</span>
    </div>
    <div class="pro-card">
      <div class="icon-ring"><svg width="54" height="54" viewBox="0 0 54 54" fill="none" stroke="#fff" stroke-width="3"><path d="M12 4v16a10 10 0 0 0 20 0V4"/><path d="M22 30v8a10 10 0 0 0 20 0v-6"/><circle cx="42" cy="26" r="5"/></svg></div>
      <h3>Certified Nursing Assistants</h3>
      <p>Caring assistants who monitor vital signs, support comfort and hygiene, and help our nurses deliver steady, attentive care to every patient.</p>
      <span class="btn-small">LEARN MORE</span>
    </div>
    <div class="pro-card">
      <div class="icon-ring"><svg width="48" height="56" viewBox="0 0 48 56" fill="none" stroke="#fff" stroke-width="3"><rect x="4" y="8" width="40" height="46" rx="3"/><rect x="15" y="3" width="18" height="10" rx="2"/><path d="M24 22v18M15 31h18"/></svg></div>
      <h3>Medical Assistants</h3>
      <p>Skilled assistants who handle intake, screening questions and records, keeping every station organized and every visit running smoothly.</p>
      <span class="btn-small">LEARN MORE</span>
    </div>
    <div class="pro-card">
      <div class="icon-ring"><svg width="56" height="50" viewBox="0 0 56 50" fill="none" stroke="#fff" stroke-width="3"><path d="M28 46S4 32 4 16A12 12 0 0 1 28 10a12 12 0 0 1 24 6c0 16-24 30-24 30z"/><path d="M12 24h10l4-7 5 13 4-6h9"/></svg></div>
      <h3>Registered Nurses</h3>
      <p>Licensed nurses who lead on-site care, assess complex cases, give clear guidance and oversee our staff at every event and workplace.</p>
      <span class="btn-small">LEARN MORE</span>
    </div>
  </div>
</section>

<section class="services">
  <div class="services-photo" role="img" aria-label="Clinic treatment room tinted in blue"></div>
  <h2 class="section-title heading">OUR MAIN SERVICES</h2>
  <p class="services-intro">From a single workplace to a weekend festival, we plan coverage around your needs. Tell us about your event or business and we will prepare a clear quote with the right staff, equipment and screening for your crowd.</p>
  <div class="service-row">
    <div><div class="ring"><svg width="70" height="60" viewBox="0 0 70 60" fill="none" stroke="#e0474c" stroke-width="3.5"><rect x="4" y="14" width="62" height="42" rx="4"/><path d="M24 14V6h22v8"/><path d="M35 24v22M24 35h22"/></svg></div><h3>First Aid Services</h3></div>
    <div><div class="ring"><svg width="40" height="76" viewBox="0 0 40 76" fill="none" stroke="#e0474c" stroke-width="3.5"><path d="M12 50V8a8 8 0 0 1 16 0v42a14 14 0 1 1-16 0z"/><circle cx="20" cy="61" r="6" fill="#e0474c"/><path d="M20 55V26"/></svg></div><h3>Covid-19 Pre Screen and Temperatures</h3></div>
    <div><div class="ring"><svg width="56" height="74" viewBox="0 0 56 74" fill="none" stroke="#e0474c" stroke-width="3.5"><circle cx="28" cy="26" r="22"/><circle cx="28" cy="26" r="13"/><path d="M16 44l-6 26 12-6 6 8 4-26M40 44l6 26-12-6"/></svg></div><h3>Training/Certifications</h3></div>
  </div>
</section>

<section class="testimonials">
  <h2 class="section-title heading">CLIENT TESTIMONIALS</h2>
  <span class="qmark" style="left:150px">&ldquo;</span><span class="qmark" style="right:150px">&rdquo;</span>
  <div class="client-photo" role="img" aria-label="Portrait of a smiling client"></div>
  <p class="quote">The team covered our three-day county fair without a single gap. They were friendly, calm and always ready, and the screening tent kept lines moving. Our vendors and guests felt safe the whole weekend, and we have already booked them again for next summer.</p>
  <p class="client-name">DANIEL HARPER</p>
  <div class="dots"><span class="on"></span><span></span><span></span></div>
</section>

<footer>
  <div class="site-footer">
    <div class="footer-col quick">
      <h4>Quick Links</h4>
      <ul><li>Home</li><li>Site Map</li><li>About Us</li><li>Blog</li><li>Our Professionals</li><li>Testimonials</li><li>Main Services</li><li>Contact Us</li></ul>
    </div>
    <div class="footer-col contact">
      <h4>Contact Us</h4>
      <div class="contact-line"><svg width="16" height="20" viewBox="0 0 16 20"><path d="M8 1a7 7 0 0 0-7 7c0 5 7 11 7 11s7-6 7-11a7 7 0 0 0-7-7z" fill="#cfd1d6"/><circle cx="8" cy="8" r="2.5" fill="#2b2c30"/></svg><span>120 Maple Street, Suite 4<br>Harrow Falls, State 00000</span></div>
      <div class="contact-line"><svg width="16" height="16" viewBox="0 0 16 16"><path d="M3 1l3 3-2 2c1 2 3 4 5 5l2-2 3 3-2 3C6 15 1 10 1 3z" fill="#cfd1d6"/></svg><span>555-014-2290</span></div>
      <div class="contact-line"><svg width="16" height="14" viewBox="0 0 16 14"><rect x="1" y="1" width="14" height="12" fill="none" stroke="#cfd1d6" stroke-width="1.6"/><path d="M1 1l7 6 7-6" fill="none" stroke="#cfd1d6" stroke-width="1.6"/></svg><span>hello@kmtmedical.example</span></div>
    </div>
    <div class="footer-col connect">
      <h4>Connect With Us</h4>
      <div class="social"><span></span><span></span><span></span><span></span></div>
      <div class="footer-badge"></div>
    </div>
  </div>
  <div class="footer-bottom"><span>Copyright &copy; 2020 KMT Medical Services. All rights reserved.</span><span>Terms and Conditions | Privacy Policy</span></div>
</footer>

</body>
</html>
```